Cosmetic Clinic Looking For Sign Designs

We are looking for sign design ideas for the front of our building and a lawn sign for our cosmetic injection salon.
I have uploaded the front of our building for a mock up and size, lawn posts with size and a sign that uses the same dimensions.
We would like both signs to be black for the background.

Target Market(s)

Ages 18-75

Industry/Entity Type

Beauty

Requirements
Must have
• Services we offer:
• Cosmetic Injections
• Airbrush Spray Tanning
• Eyelash Growth Serum
• Skin Care Products & More
• Everything must be on a black background
• The lawn sign must have the address: 394 Fenwick and the building sign should have the phone number.
Should not have
• Nothing can light up (no LED)
• Both signs do not need the full address. Just 394 Fenwick and the phone number

```html
<!DOCTYPE html>
<html lang="en">
<head>
<meta charset="utf-8">
<title>Averly Beauty – Lawn Sign</title>
<link rel="stylesheet" href="https://fonts.googleapis.com/css2?family=Barlow:wght@500;600&display=swap">
<style>
  :root {
    --backdrop: #e9e8ee;
    --sign-black: #0d0d0f;
    --lavender: #9b93d6;
    --teal: #2a9fb5;
    --pink: #ef1f7d;
    --ink: #111114;
  }
  html, body {
    margin: 0;
    padding: 0;
    width: 1200px;
    height: 1086px;
    overflow: hidden;
    background: var(--backdrop);
  }
  .canvas {
    position: relative;
    width: 1200px;
    height: 1086px;
  }
  .lawn-sign {
    position: absolute;
    left: 124px;
    top: 43px;
    width: 952px;
    height: 1000px;
  }
  .sign-body { fill: var(--sign-black); }
  .sign-border { fill: none; stroke: var(--lavender); stroke-width: 5; }
  .brand-dot { fill: var(--lavender); }
  .brand-name {
    font-family: "Barlow", sans-serif;
    font-weight: 600;
    font-size: 58px;
    letter-spacing: 2px;
    fill: var(--teal);
  }
  .service-pill { fill: var(--lavender); }
  .service-label {
    font-family: "Barlow", sans-serif;
    font-weight: 500;
    font-size: 22px;
    fill: var(--ink);
  }
  .contact-panel { fill: var(--pink); }
  .contact-address {
    font-family: "Barlow", sans-serif;
    font-weight: 500;
    font-size: 24px;
    fill: var(--ink);
  }
  .contact-phone {
    font-family: "Barlow", sans-serif;
    font-weight: 500;
    font-size: 36px;
    letter-spacing: 1px;
    fill: var(--ink);
  }
</style>
</head>
<body>
<main class="canvas">
  <svg class="lawn-sign" viewBox="0 0 595 625" role="img" aria-label="Averly Beauty lawn sign">
    <path class="sign-body" d="M0,95 L95,95 Q297,-95 500,95 L595,95 L595,580 Q550,580 545,625 L50,625 Q45,580 0,580 Z"/>
    <path class="sign-border" d="M12,105 L100,105 Q297,-81 495,105 L583,105 L583,572 Q540,572 535,613 L60,613 Q55,572 12,572 Z"/>

    <circle class="brand-dot" cx="297" cy="118" r="56"/>

    <text class="brand-name" x="297" y="270" text-anchor="middle">AVERLY BEAUTY</text>

    <g class="service-list">
      <rect class="service-pill" x="82" y="325" width="430" height="30" rx="15"/>
      <text class="service-label" x="297" y="348" text-anchor="middle">COSMETIC INJECTIONS</text>
      <rect class="service-pill" x="82" y="363" width="430" height="30" rx="15"/>
      <text class="service-label" x="297" y="386" text-anchor="middle">AIRBRUSH SPRAY TANNING</text>
      <rect class="service-pill" x="82" y="400" width="430" height="30" rx="15"/>
      <text class="service-label" x="297" y="423" text-anchor="middle">EYELASH GROWTH SERUM</text>
      <rect class="service-pill" x="82" y="438" width="430" height="30" rx="15"/>
      <text class="service-label" x="297" y="461" text-anchor="middle">SKIN CARE PRODUCTS &amp; MORE</text>
    </g>

    <path class="contact-panel" d="M28,508 Q28,493 43,493 L550,493 Q565,493 565,508 L565,558 Q540,560 535,593 L60,593 Q55,560 28,558 Z"/>
    <text class="contact-address" x="297" y="528" text-anchor="middle">394 Fenwick Street, Lakeview, ON K3M 2P4</text>
    <text class="contact-phone" x="297" y="575" text-anchor="middle">(555) 214 7390</text>
  </svg>
</main>
</body>
</html>
```